International Supplier needs an eye catching profssional letterhead and continuation page

We need a letterhead and continuation sheet designed for a company based in Austria called VELMA Screens GmbH. We develop and install innovate glass partition wall solutions to commercial and cultural buildings and to some of the most contemporary architectural buildings in Europe. I have our inhouse design brief confirming our corporate colours, fonts and images and have our corporate logo available in a variety of formats including AI and EPS. We are open to differing design suggestions as long as they follow the colour and font specification in our corporate design brief. We are at the forefront of innovation, craftmanship and design for architectural glass, framing systems and fire rated partition systems. The final design should communicate the spirit and strength of the company.
www.velma.com / www.tarnovu.co.uk / www.brandpane.com

Target Market(s)

Architects, planners, designers, building contractors and construction companies

Industry/Entity Type

Architecture

Font styles to use
Sans Serif

Requirements
Must have
• VELMA Screens GmbH
• Lindorfergasse 4 B
• 7291 Marbach am Feld
• Südmark
• Tel: +43 (1) 482 6170
• E-mail:office@velmascreens.at
• Web:www.velmascreens.at / www.velmabrandpane.com
• subtle yet professionally distinctive
• colours and fonts to be taken ffom VELMA design guide but we are also open to variations on the same theme
Should not have
• No bold lines

```html
<!DOCTYPE html>
<html lang="de">
<head>
<meta charset="utf-8">
<title>VELMA Screens GmbH – Briefpapier</title>
<link href="https://fonts.googleapis.com/css2?family=Questrial&display=swap" rel="stylesheet">
<style>
  :root {
    --backdrop: #cfcfcf;
    --paper: #f3f3f3;
    --brand-red: #b22543;
    --ink: #1e1e1e;
    --ink-soft: #555555;
  }
  * { box-sizing: border-box; margin: 0; padding: 0; }
  html, body {
    width: 1200px;
    height: 780px;
    overflow: hidden;
    background: var(--backdrop);
    font-family: "Questrial", "Century Gothic", sans-serif;
  }
  .letterhead {
    position: absolute;
    left: 340px;
    top: 22px;
    width: 520px;
    height: 736px;
    background: var(--paper);
    box-shadow: 0 2px 10px rgba(0,0,0,0.12);
    overflow: hidden;
  }
  .brand {
    position: absolute;
    top: 46px;
    left: 0;
    width: 100%;
    display: flex;
    justify-content: center;
    align-items: center;
    gap: 5px;
  }
  .brand-square {
    width: 24px;
    height: 24px;
    background: var(--brand-red);
  }
  .brand-name {
    font-size: 33px;
    letter-spacing: 0.5px;
    color: var(--ink);
    line-height: 1;
  }
  .corner-block {
    position: absolute;
    right: 0;
    bottom: 0;
    width: 80px;
    height: 131px;
    background: var(--brand-red);
  }
  .footer {
    position: absolute;
    left: 0;
    width: 100%;
    top: 694px;
    text-align: center;
    font-size: 7px;
    color: var(--ink-soft);
    line-height: 11px;
  }
  .footer .company { color: var(--brand-red); font-weight: 700; }
  .footer .sep { margin: 0 3px; }
  .contact-line { display: flex; justify-content: center; align-items: center; }
  .contact-item { display: inline-flex; align-items: center; gap: 2px; }
  .contact-item svg { width: 7px; height: 7px; fill: none; stroke: var(--brand-red); stroke-width: 1.4; }
</style>
</head>
<body>
  <main class="letterhead">
    <header class="brand">
      <span class="brand-square"></span>
      <span class="brand-name">VELMA</span>
    </header>

    <footer class="footer">
      <div class="address-line">
        <span class="company">VELMA Screens GmbH</span><span class="sep">|</span>Lindorfergasse 4 B<span class="sep">|</span>7291 Marbach am Feld<span class="sep">|</span>Südmark
      </div>
      <div class="contact-line">
        <span class="contact-item">
          <svg viewBox="0 0 10 10"><path d="M2 1 L4 1 L4.6 3 L3.4 4 Q4.5 6 6 6.6 L7 5.4 L9 6 L9 8 Q5 9 2 6 Q1 4 2 1 Z"/></svg>
          +43 (1) 482 6170
        </span>
        <span class="sep">|</span>
        <span class="contact-item">
          <svg viewBox="0 0 10 10"><rect x="1" y="2.2" width="8" height="5.6"/><path d="M1 2.2 L5 5.4 L9 2.2"/></svg>
          office@velmascreens.at
        </span>
        <span class="sep">|</span>
        <span class="contact-item">
          <svg viewBox="0 0 10 10"><circle cx="5" cy="5" r="4"/><path d="M1 5 H9 M5 1 Q2.5 5 5 9 Q7.5 5 5 1"/></svg>
          www.velmascreens.at
        </span>
        <span class="sep">|</span>
        <span class="contact-item">
          <svg viewBox="0 0 10 10"><circle cx="5" cy="5" r="4"/><path d="M1 5 H9 M5 1 Q2.5 5 5 9 Q7.5 5 5 1"/></svg>
          www.velmabrandpane.com
        </span>
      </div>
    </footer>

    <div class="corner-block"></div>
  </main>
</body>
</html>
```